Building and Facilities Management brochure

Please refer to attached PDF, page by page with information about the brief.
SOPHISTICATED, BOLD, PROFESSIONAL BROCHURE to market our company in business meetings to Builders, Owners of buildings, Strata Committees etc.

The final design should portray quality, service, integrity,
Clear Communication

Attached is:
- pdf with details of basic layout options and wording and most of the information about the brief.
- Logo options to use
- Business card designs to understand what design we have previously had.
- Word document of the pdf if that helps to copy the information.

Target Market(s)

Professionals. Builders/developer, Strata Owners, and Building owners who want a high level of service and management of their building

Industry/Entity Type

It Company

Requirements
Must have
• - Logo
• - Contact details
• - Use of the colour in the design which has been specified.
• - Images/s of building/s
• - Use the phrase "Quality Service with Integrity"
Nice to have
• - as much of the wording as possible from the document which was uploaded, that will fit and work with the design
Should not have
• Excessive colour or variances as it needs to stay clear, bold and sophisticated.
• Too much on the page, clarity is key for clear communication without trying to clutter too much on the page.

```html
<!DOCTYPE html>
<html lang="en">
<head>
<meta charset="utf-8">
<title>Tidewell Facility Group – Brochure</title>
<link rel="stylesheet" href="https://fonts.googleapis.com/css2?family=Oswald:wght@400;600&family=Open+Sans:wght@400;600;700&display=swap">
<style>
  :root {
    --page-bg: #3b3b3d;
    --navy-dark: #1c222b;
    --navy: #2a323d;
    --blue: #2f7fd0;
    --blue-bright: #4aa3ea;
    --sky-mid: #8fbde6;
    --white: #ffffff;
    --text-dark: #2b2f36;
    --text-muted: #8a93a0;
    --text-light: #c7cfd9;
  }
  * { box-sizing: border-box; margin: 0; padding: 0; }
  html, body { width: 1200px; height: 1000px; overflow: hidden; }
  body {
    background: var(--page-bg);
    font-family: "Open Sans", Arial, sans-serif;
    color: var(--text-dark);
    position: relative;
  }
  .sheet {
    position: absolute;
    left: 50px;
    width: 1100px;
    display: flex;
    box-shadow: 0 10px 30px rgba(0,0,0,.45);
    overflow: hidden;
  }
  .sheet--outside { top: 36px; height: 420px; }
  .sheet--inside { top: 490px; height: 470px; background: var(--white); flex-direction: column; }

  /* ---------- Outside ---------- */
  .panel { flex: 1; position: relative; }
  .panel--photo {
    background: linear-gradient(175deg, #e4f0fa 0%, #8dbbe4 45%, #2f6fae 75%, #183a60 100%);
  }
  .panel--dark {
    background: linear-gradient(160deg, var(--navy) 0%, var(--navy-dark) 100%);
    border-left: 1px solid rgba(255,255,255,.06);
    display: flex; flex-direction: column; align-items: center; justify-content: center;
    text-align: center; color: var(--white);
    padding: 0 30px;
  }
  .brand-name {
    font-family: "Open Sans", Arial, sans-serif;
    font-weight: 600;
    color: var(--blue-bright);
    letter-spacing: 1px;
  }
  .brand-name--large { font-size: 24px; line-height: 1.3; }
  .tagline { margin-top: 14px; font-size: 11px; letter-spacing: 2px; text-transform: uppercase; color: var(--sky-mid); }
  .contact-list { list-style: none; margin-top: 16px; font-size: 11px; line-height: 1.9; color: var(--text-light); }

  /* ---------- Inside ---------- */
  .hero { height: 235px; display: flex; position: relative; }
  .hero-scene {
    flex: 2;
    background: linear-gradient(180deg, #f2f8fd 0%, #bcd9f1 50%, #7fb1df 100%);
    position: relative;
  }
  .hero-collage {
    flex: 1;
    background: linear-gradient(135deg, #dfe7ee 0%, #9fb7cc 50%, #6f8ea9 100%);
    border-left: 4px solid var(--white);
  }
  .section-title {
    font-family: "Oswald", Arial, sans-serif;
    font-weight: 600;
    text-transform: uppercase;
    color: var(--blue);
    font-size: 26px;
    border-left: 3px solid var(--blue);
    padding-left: 10px;
    line-height: 1;
  }
  .section-title--small { font-size: 20px; margin-bottom: 10px; }
  .vision-box {
    position: absolute; left: 0; top: 70px; width: 330px; height: 165px;
    background: linear-gradient(180deg, rgba(36,112,196,.92), rgba(26,84,156,.95));
    color: var(--white); padding: 16px 20px;
  }
  .vision-box .section-title { color: var(--white); border-color: var(--white); margin-bottom: 10px; }
  .vision-box p { font-size: 10px; line-height: 1.55; margin-bottom: 6px; }
  .services-title { position: absolute; left: 390px; top: 40px; }
  .service-labels {
    position: absolute; left: 400px; top: 95px;
    font-family: "Oswald", Arial, sans-serif; font-weight: 600; color: var(--navy-dark);
    font-size: 22px; line-height: 1; text-transform: uppercase;
  }
  .service-labels span {
    display: block; font-family: "Open Sans", Arial, sans-serif; font-weight: 600;
    font-size: 8px; letter-spacing: 1px; color: var(--text-dark); margin: 2px 0 10px;
  }

  .content { flex: 1; display: flex; padding: 20px 24px 10px; gap: 28px; }
  .column { flex: 1; }
  .column h3 {
    font-size: 11px; font-weight: 700; text-transform: uppercase; color: var(--blue); margin-bottom: 6px; letter-spacing: .5px;
  }
  .column p { font-size: 10px; line-height: 1.5; margin-bottom: 6px; }
  .key-list { list-style: none; font-size: 10px; line-height: 1.5; }
  .key-list li { margin-bottom: 5px; }
  .key-list strong { color: var(--blue); text-transform: uppercase; font-size: 9px; }
  .service-list { list-style: none; font-size: 10px; font-weight: 700; line-height: 1.7; text-transform: uppercase; color: var(--navy-dark); margin-bottom: 12px; }
  .service-list li::before { content: ""; display: inline-block; width: 5px; height: 5px; background: var(--blue); margin-right: 7px; vertical-align: middle; }
  .caption { font-size: 10px; color: var(--text-muted); font-style: italic; }

  .footer {
    height: 48px; background: linear-gradient(90deg, var(--navy-dark), var(--navy));
    border-top: 3px solid var(--blue);
    display: flex; align-items: center; justify-content: space-between; padding: 0 24px;
  }
  .brand-name--small { font-size: 13px; }
  .footer-web { font-size: 11px; color: #aeb8c4; letter-spacing: 1px; }
</style>
</head>
<body>

  <section class="sheet sheet--outside">
    <div class="panel panel--photo" role="img" aria-label="City skyline with bridge and river in blue tones"></div>
    <div class="panel panel--dark">
      <div class="brand-name brand-name--large">Tidewell Facility Group</div>
      <div class="tagline">Quality Service with Integrity</div>
    </div>
    <div class="panel panel--dark">
      <div class="brand-name brand-name--large">Tidewell Facility Group</div>
      <ul class="contact-list">
        <li>Phone 02 5550 1840</li>
        <li>info@tidewellfacility.com.au</li>
        <li>Suite 4, 20 Market Lane, Sydney</li>
        <li>www.tidewellfacility.com.au</li>
      </ul>
    </div>
  </section>

  <section class="sheet sheet--inside">
    <div class="hero">
      <div class="hero-scene" role="img" aria-label="Businessman overlooking a misty blue city skyline">
        <div class="vision-box">
          <h2 class="section-title">Vision</h2>
          <p>Our vision is to deliver building and facilities management that owners trust, with clear reporting, prompt response and care for every asset we manage.</p>
          <p>We partner with builders, strata committees and owners to protect value and keep every property running smoothly.</p>
        </div>
        <h2 class="section-title services-title">Services</h2>
        <div class="service-labels">
          Core<span>Services</span>
          Value<span>Added Services</span>
        </div>
      </div>
      <div class="hero-collage" role="img" aria-label="Collage of building plans, a handshake and a site worker in a hard hat"></div>
    </div>

    <div class="content">
      <div class="column">
        <h2 class="section-title section-title--small">Key Aspects</h2>
        <ul class="key-list">
          <li><strong>Compliance</strong> – every site meets current codes and safety standards.</li>
          <li><strong>Preventative maintenance</strong> – planned works that reduce costly repairs.</li>
          <li><strong>Communication</strong> – regular updates and one point of contact.</li>
          <li><strong>Relationships</strong> – long-term partners, contractors and trades we trust.</li>
        </ul>
      </div>
      <div class="column">
        <h3>Core Services</h3>
        <p>Tailored services for residential and commercial buildings of every size.</p>
        <ul class="service-list">
          <li>Building Management</li>
          <li>Facilities Management</li>
          <li>Maintenance Planning</li>
          <li>Contractor Coordination</li>
        </ul>
      </div>
      <div class="column">
        <h3>Value Added Services</h3>
        <p>Extra support that adds long-term value to your property.</p>
        <ul class="service-list">
          <li>Defect Management</li>
          <li>Energy Audits</li>
          <li>Capital Works Planning</li>
          <li>Building Reports</li>
        </ul>
        <p class="caption">Trusted by owners and committees across the city.</p>
      </div>
    </div>

    <footer class="footer">
      <div class="brand-name brand-name--small">Tidewell Facility Group</div>
      <div class="footer-web">www.tidewellfacility.com.au</div>
      <div class="brand-name brand-name--small">Tidewell Facility Group</div>
    </footer>
  </section>

</body>
</html>
```